Flyer Rework for Accountants and Lawyers

Information flyer for accountants and lawyers. Text and flowchart provided. Just need to make it look presentable for print and email. Needs to add logo (AI file provided) and provide graphics. No more than two pages. Our corporate visual identify guidelines are attached (MUST Use). Completed on both AI file and PPTX file.
Target Market(s)
Accountants, Company Directors and Lawyers
Industry/Entity Type
Finance And Accounting
Requirements
Must have
- Our corporate visual identify guidelines are attached (MUST Use)

```html
<!DOCTYPE html>
<html lang="en">
<head>
<meta charset="utf-8">
<title>Northfield Advisory – Corporate Visual Identity</title>
<link href="https://fonts.googleapis.com/css2?family=Figtree:wght@400;500;600;700;800&display=swap" rel="stylesheet">
<style>
  :root {
    --backdrop: #959595;
    --paper: #ffffff;
    --brand-green: #6cb443;
    --brand-dark: #333333;
    --ink: #3a3a3a;
    --ink-soft: #6d6d6d;
    --table-fill: #ececec;
  }
  * { box-sizing: border-box; margin: 0; padding: 0; }
  html, body { width: 1200px; height: 1200px; overflow: hidden; }
  body {
    background: var(--backdrop);
    font-family: "Figtree", "Helvetica Neue", Arial, sans-serif;
    color: var(--ink);
    position: relative;
  }
  .page {
    position: absolute;
    left: 245px;
    width: 710px;
    height: 502px;
    background: var(--paper);
    overflow: hidden;
  }
  .page--cover { top: 82px; }
  .page--facts { top: 618px; }
  .page svg.shapes { position: absolute; inset: 0; width: 710px; height: 502px; }
  .abs { position: absolute; }

  /* Cover */
  .cover-kicker {
    left: 25px; top: 135px;
    font-size: 25px; font-weight: 400; color: #fff; letter-spacing: 0.2px;
  }
  .cover-date {
    left: 25px; top: 200px;
    font-size: 40px; font-weight: 700; color: #fff; letter-spacing: 0.3px;
  }
  .cover-tagline {
    left: 25px; top: 245px;
    font-size: 15.5px; font-weight: 700; color: var(--brand-dark);
  }
  .brand-name {
    left: 513px; top: 410px;
    font-size: 14.5px; font-weight: 600; color: var(--ink-soft); letter-spacing: 0.2px;
  }
  .brand-sub {
    left: 522px; top: 427px;
    font-size: 7.6px; font-weight: 500; color: var(--ink-soft);
  }

  /* Facts page */
  .facts-title {
    left: 31px; top: 59px;
    font-size: 14.5px; font-weight: 700; line-height: 19px; color: var(--brand-dark);
  }
  .facts-body {
    left: 31px; top: 108px; width: 380px;
    font-size: 9.5px; line-height: 12.2px; text-align: justify;
  }
  .facts-body p + p { margin-top: 12px; }
  .facts-body strong { font-weight: 700; color: var(--brand-dark); }
  .table-head {
    top: 263px; font-size: 9.2px; font-weight: 700; color: var(--brand-dark);
  }
  .cell {
    font-size: 6.3px; line-height: 8px; color: var(--ink);
  }
  .cell--fact { left: 38px; width: 120px; }
  .cell--detail { left: 191px; width: 200px; }
</style>
</head>
<body>

<section class="page page--cover" aria-label="Cover page">
  <svg class="shapes" viewBox="0 0 710 502" aria-hidden="false">
    <defs>
      <linearGradient id="teamTone" x1="0" y1="0" x2="1" y2="1">
        <stop offset="0" stop-color="#9a9a9a"/>
        <stop offset="0.5" stop-color="#c9c9c9"/>
        <stop offset="1" stop-color="#6f6f6f"/>
      </linearGradient>
    </defs>
    <polygon points="0,114 347,114 318,187 0,187" fill="var(--brand-dark)"/>
    <polygon points="0,187 315,187 271,286 0,286" fill="var(--brand-green)"/>
    <polygon points="331,146 710,146 710,370 245,370" fill="url(#teamTone)" role="img" aria-label="Black and white photo of a team of four colleagues gathered around a table looking at a phone"/>
    <line x1="405" y1="0" x2="218" y2="474" stroke="var(--brand-green)" stroke-width="2.4"/>
    <circle cx="478" cy="432" r="33" fill="none" stroke="var(--ink-soft)" stroke-width="4"/>
  </svg>
  <div class="abs cover-kicker">Corporate Visual Identity</div>
  <div class="abs cover-date">August 2018</div>
  <div class="abs cover-tagline">Our Brand is Our Responsibility</div>
  <div class="abs brand-name">NORTHFIELD ADVISORY</div>
  <div class="abs brand-sub">Restructuring &amp; Solvency Accountants</div>
</section>

<section class="page page--facts" aria-label="Director Penalty Notice facts">
  <svg class="shapes" viewBox="0 0 710 502">
    <defs>
      <linearGradient id="deskTone" x1="0" y1="0" x2="1" y2="1">
        <stop offset="0" stop-color="#6b5a48"/>
        <stop offset="0.45" stop-color="#e9ecef"/>
        <stop offset="0.75" stop-color="#cfd9e2"/>
        <stop offset="1" stop-color="#8a6a55"/>
      </linearGradient>
    </defs>
    <polygon points="471,0 710,0 710,502 386,502" fill="url(#deskTone)" role="img" aria-label="Photo of hands with a pen reviewing printed charts beside a laptop"/>
    <polygon points="27,282 654,282 624,477 27,477" fill="var(--table-fill)"/>
    <polygon points="27,258 660,258 654,282 27,282" fill="var(--brand-green)"/>
    <line x1="168" y1="258" x2="168" y2="477" stroke="var(--brand-dark)" stroke-width="1"/>
  </svg>

  <h1 class="abs facts-title">NORTHFIELD ADVISORY<br>INDEPENDENT. CONCISE. EFFICIENT.</h1>

  <div class="abs facts-body">
    <p>Company directors and their advisors need to be aware that non-lodgement of Business Activities Statements (“BAS”) and Superannuation Guarantee Charge (“SCG”) Statements with the ATO may be personally liability for these debts.</p>
    <p><strong>Director Penalty Notices (“DPN”)</strong><br>
    The ATO uses DPNs and Garnishee Notices to recovery tax debts and to impose positive obligations on Directors to deal with outstanding PAYG Withholding and the Superannuation Guarantee Charge debts (“Tax Debts”).<br>
    The DPN regime makes directors of companies who fail to pay Tax Debts personally liable. The key facts of DPN regime are outlined below:</p>
  </div>

  <div class="abs table-head" style="left:38px;">Facts</div>
  <div class="abs table-head" style="left:191px;">Key facts of a Directors Penalty Notice</div>

  <div class="abs cell cell--fact" style="top:298px;">1.&nbsp; Director personal liabilities</div>
  <div class="abs cell cell--detail" style="top:294px;">Directors become personally liable for Tax Debts 21 days are the DPN Notice is issued</div>

  <div class="abs cell cell--fact" style="top:328px;">2. Automatic liability for unreported and unpaid Tax Debts</div>
  <div class="abs cell cell--detail" style="top:326px;">Where a company’s Tax Debts were both unreported and unpaid 3 months after the due date, the directors are automatically personally liable for the Tax Debts.</div>

  <div class="abs cell cell--fact" style="top:361px;">3. Avoiding personal liability for directors once they receive a DPN</div>
  <div class="abs cell cell--detail" style="top:358px;">Within 21 days of issuing the DPN (which may be received a week or more after issue), a director can avoid personal liability by either:<br>Paying the Tax Debt<br>Appointing an Administrator to the company<br>Appointing a Liquidator to the company</div>

  <div class="abs cell cell--fact" style="top:413px;">4. Effect on new directors</div>
  <div class="abs cell cell--detail" style="top:410px;">New directors are liable if outstanding Tax Debts are unpaid 30 days after their appointment as director</div>

  <div class="abs cell cell--fact" style="top:440px;">5. Time frames</div>
  <div class="abs cell cell--detail" style="top:437px;">ATO can only enforce a DPN after 21 days of giving notice to the director and notice can be given to the company tax agent</div>
</section>

</body>
</html>
```